Workforce Equity Lens Poster for staff

Our organization has developed an equity lens to be used by staff when implementing new programs and services. We need a poster that will be used as a quick reference for staff to use on a daily basis and will hang in cubicles. We'd like the main six questions to stand out with the subsequent questions less prominent. Looking for a poster that is 11 x 17 inches.

Industry/Entity Type

Equity

Font styles to use
Sans Serif

Colors

Designer to choose colors to be used in the design.

Requirements
Must have
• Easy to read. Not too text heavy, so any way to highlight the main six questions. It would be great to have some sort of icon or illustration with each of the six questions.
Nice to have
• Illustrative design features.
Should not have
• No photos of people.

```html
<!DOCTYPE html>
<html lang="en">
<head>
<meta charset="utf-8">
<title>Equity Lens Poster</title>
<link rel="stylesheet" href="https://fonts.googleapis.com/css2?family=Roboto+Condensed:wght@400;700&display=swap">
<style>
  :root {
    --backdrop: #161616;
    --paper: #ffffff;
    --header-bg: #f3f3f3;
    --card-bg: #f3f3f3;
    --brand-blue: #1a6cb8;
    --wave-light: #2a8fd6;
    --accent-green: #95b53a;
    --ink: #111111;
  }
  * { box-sizing: border-box; margin: 0; padding: 0; }
  html, body {
    width: 1200px; height: 1200px; overflow: hidden;
    background: var(--backdrop);
    font-family: "Roboto Condensed", "Arial Narrow", sans-serif;
  }
  .poster {
    position: absolute; left: 221px; top: 15px;
    width: 948px; height: 1464px;
    transform: scale(0.7992); transform-origin: top left;
    background: var(--paper); overflow: hidden;
  }
  .poster-header {
    position: absolute; left: 0; top: 0; width: 948px; height: 146px;
    background: var(--header-bg);
    border-bottom: 8px solid var(--accent-green);
  }
  .brand { position: absolute; left: 46px; top: 36px; display: flex; align-items: center; gap: 22px; }
  .brand-mark { width: 76px; height: 76px; border-radius: 50%; background: var(--brand-blue); }
  .brand-name {
    color: var(--brand-blue); font-weight: 700; font-size: 38px; line-height: 1.05;
    letter-spacing: 1px; text-transform: uppercase;
  }
  .brand-name span { display: block; font-size: 26px; letter-spacing: 12px; }
  .header-divider { position: absolute; left: 584px; top: 22px; width: 4px; height: 102px; background: var(--brand-blue); }
  .poster-title {
    position: absolute; left: 634px; top: 44px;
    color: var(--brand-blue); font-weight: 700; font-size: 46px; letter-spacing: 0.5px;
  }
  .wave { position: absolute; left: 0; top: 0; width: 948px; height: 1464px; }
  .question {
    position: absolute; left: 46px; width: 856px;
    background: var(--card-bg); border-radius: 4px;
    padding: 14px 20px 0 20px;
  }
  .question h2 {
    color: var(--accent-green); font-weight: 700; font-size: 38px; line-height: 1.12;
    text-transform: uppercase; letter-spacing: 0.2px;
  }
  .question p { color: var(--ink); font-weight: 700; font-size: 23.5px; line-height: 1.24; margin-top: 2px; }
</style>
</head>
<body>
<main class="poster">
  <svg class="wave" viewBox="0 0 948 1464" aria-hidden="true">
    <path d="M0 1258 C260 1370 600 1396 948 1386 L948 1464 L0 1464 Z" fill="var(--wave-light)"/>
    <path d="M0 1282 C260 1388 600 1410 948 1404 L948 1464 L0 1464 Z" fill="var(--brand-blue)"/>
  </svg>

  <header class="poster-header">
    <div class="brand">
      <div class="brand-mark"></div>
      <div class="brand-name">Ridgeway Workforce<span>Alliance</span></div>
    </div>
    <div class="header-divider"></div>
    <h1 class="poster-title">EQUITY LENS</h1>
  </header>

  <section class="question" style="top:284px;height:170px">
    <h2>1. Who is affected?</h2>
    <p>Who are the groups affected by this policy, metric, program, decision, or proposed action? How will each group be affected? Is any group negatively affected in a disproportionate way?</p>
  </section>
  <section class="question" style="top:467px;height:170px">
    <h2>2. Are they at the table?</h2>
    <p>How have you actively involved stakeholders who are also members of the communities affected by the policy, metric, program, decision, or proposed action?</p>
  </section>
  <section class="question" style="top:649px;height:136px">
    <h2>3. What are the barriers?</h2>
    <p>What are the societal or organizational barriers that prevent a population from being successful?</p>
  </section>
  <section class="question" style="top:798px;height:180px">
    <h2>4. What are population-specific strategies?</h2>
    <p>To address any inequities, do we have solutions that are tailored to work for the disproportionately affected groups?&nbsp; Have we used the ‘Platinum Rule’?</p>
  </section>
  <section class="question" style="top:991px;height:132px">
    <h2>5. Are there unintended consequences?</h2>
    <p>Does this policy, program, decision, or proposed action ignore or worsen existing disparities or produce other unintended consequences?</p>
  </section>
  <section class="question" style="top:1136px;height:198px">
    <h2>6. How do we measure success in a population-specific way?</h2>
    <p>Describe how data about the policy, metric, program, decision, or proposed action, and its impact (positive or negative) on equitable access and outcomes, will be monitored and evaluated?</p>
  </section>
</main>
</body>
</html>
```